Whitmore Business Card Design

The name of the business is Dara Whitmore, CPA LLC
The service that we offer is Accounting, Tax & Consulting Services. I need it to have the following items:
Dara Whitmore, Principal
Phone Number
Email Address
Physical Address

I have attached the company logo, one in black and one in white. Please provide a design in black background and the other in white background. Please include "Accounting, Tax & Consulting Services". I want the business card to be clean and very professional.

```html
<!DOCTYPE html>
<html lang="en">
<head>
<meta charset="UTF-8">
<title>Dara Whitmore, CPA LLC – Business Cards</title>
<link href="https://fonts.googleapis.com/css2?family=Montserrat:wght@500;600;700&family=Arimo:wght@400;700&display=swap" rel="stylesheet">
<style>
  :root {
    --backdrop: #2b2b2b;
    --card: #ffffff;
    --ink: #3a3a3c;
    --grey: #9a9a9c;
    --red: #a31c22;
    --rule: #c9c9c9;
  }
  * { box-sizing: border-box; margin: 0; padding: 0; }
  html, body { width: 1200px; height: 900px; overflow: hidden; }
  body {
    background: var(--backdrop);
    font-family: "Arimo", Arial, sans-serif;
    color: var(--ink);
    position: relative;
  }
  .card {
    position: absolute;
    left: 300px;
    width: 600px;
    height: 343px;
    background: var(--card);
    border-radius: 14px;
    overflow: hidden;
  }
  .card--front { top: 70px; }
  .card--back { top: 478px; }

  .brand {
    display: flex;
    align-items: center;
    gap: 12px;
  }
  .brand__mark {
    width: 14px; height: 14px;
    background: var(--red);
    flex: none;
  }
  .brand__name {
    font-family: "Montserrat", sans-serif;
    font-weight: 600;
    font-size: 30px;
    letter-spacing: 0.5px;
    color: var(--ink);
    text-transform: uppercase;
    white-space: nowrap;
  }
  .brand__tagline {
    font-family: "Montserrat", sans-serif;
    font-weight: 600;
    font-size: 15px;
    letter-spacing: 3px;
    color: var(--grey);
    text-transform: uppercase;
    margin-top: 4px;
  }

  /* Front */
  .card--front .brand-block {
    position: absolute;
    left: 0; right: 0; top: 118px;
    display: flex; flex-direction: column; align-items: center;
  }
  .services {
    position: absolute;
    left: 0; right: 0; top: 214px;
    text-align: center;
    font-size: 16px;
    color: #222;
  }

  /* Back */
  .card--back .brand-block {
    position: absolute;
    left: 70px; top: 56px;
  }
  .card--back .brand__name { font-size: 26px; }
  .card--back .brand__tagline { font-size: 13px; letter-spacing: 2.6px; }
  .person {
    position: absolute;
    left: 70px; top: 150px;
    width: 210px;
    text-align: right;
  }
  .person__name {
    font-family: "Montserrat", sans-serif;
    font-weight: 700;
    font-size: 24px;
    color: var(--red);
    text-transform: uppercase;
    white-space: nowrap;
  }
  .person__role { font-size: 16px; color: #222; margin-top: 2px; }
  .divider {
    position: absolute;
    left: 298px; top: 140px;
    width: 1px; height: 76px;
    background: var(--rule);
  }
  .contacts {
    position: absolute;
    left: 318px; top: 142px;
    list-style: none;
    font-size: 15px;
    color: #222;
  }
  .contacts li {
    display: flex; align-items: center; gap: 8px;
    height: 24px;
  }
  .contacts svg { width: 13px; height: 13px; flex: none; }
  .address-band {
    position: absolute;
    left: 0; right: 0; top: 252px;
    height: 44px;
    background: var(--red);
    color: #fff;
    font-size: 16px;
    display: flex; align-items: center; justify-content: center;
    letter-spacing: 0.3px;
  }
</style>
</head>
<body>

  <section class="card card--front" aria-label="Business card front">
    <div class="brand-block">
      <div class="brand">
        <span class="brand__mark"></span>
        <span class="brand__name">Dara Whitmore, CPA LLC</span>
      </div>
      <div class="brand__tagline">Certified Public Accountant</div>
    </div>
    <p class="services">Accounting, Tax &amp; Consulting Services</p>
  </section>

  <section class="card card--back" aria-label="Business card back">
    <div class="brand-block">
      <div class="brand">
        <span class="brand__mark"></span>
        <span class="brand__name">Dara Whitmore, CPA LLC</span>
      </div>
      <div class="brand__tagline">Certified Public Accountant</div>
    </div>

    <div class="person">
      <div class="person__name">Dara Whitmore</div>
      <div class="person__role">Principal</div>
    </div>

    <span class="divider"></span>

    <ul class="contacts">
      <li>
        <svg viewBox="0 0 16 16" aria-hidden="true"><path fill="#a31c22" d="M3.6 1.5l2.3 2.6-1.3 1.7c.9 2 2.6 3.7 4.6 4.6l1.7-1.3 2.6 2.3-1.4 2.3C7 13.3 2.7 9 1.3 3z"/></svg>
        555-013-2846
      </li>
      <li>
        <svg viewBox="0 0 16 16" aria-hidden="true"><rect x="1" y="3" width="14" height="10" rx="1" fill="#a31c22"/><path d="M1.5 3.8L8 9l6.5-5.2" stroke="#fff" stroke-width="1.3" fill="none"/></svg>
        info@whitmorecpa.com
      </li>
      <li>
        <svg viewBox="0 0 16 16" aria-hidden="true"><circle cx="8" cy="8" r="7" fill="#a31c22"/><path d="M1 8h14M8 1c-3 3.5-3 10.5 0 14M8 1c3 3.5 3 10.5 0 14" stroke="#fff" stroke-width="1" fill="none"/></svg>
        www.whitmorecpa.com
      </li>
    </ul>

    <div class="address-band">418 Harbor View Lane Elmsford County 7702</div>
  </section>

</body>
</html>
```